RWT General Contracting

Roofing, Siding,windows, doors, Gutter,additions, decks, garagesand hanyman services fully insured and licensed, free estimates, accept all major credit cards call (617)442-9073 email morvinkt@mailbrook.net

Target Market(s)

Home improvement

Industry/Entity Type

Home Improvement

Requirements
Must have
• Whats listed above
Nice to have
• I dont have a logo i want wording for roofing, siding, gutter, decks, additions, windows, doors, and handyman services with my phone # 617-442-9073 and email morvinkt@mailbrook.net

```html
<!DOCTYPE html>
<html lang="en">
<head>
<meta charset="utf-8">
<title>RWT General Contracting – Postcard</title>
<link href="https://fonts.googleapis.com/css2?family=Lato:wght@400;700;900&family=Tinos:wght@400&display=swap" rel="stylesheet">
<style>
  :root{
    --navy:#1b4a8a;
    --gold:#f7b514;
    --white:#ffffff;
    --ink:#2b2b2b;
    --stage-top:#4a4a4a;
    --stage-bottom:#262626;
    --deck:#b97f4c;
    --siding:#c9c8b8;
    --lawn:#6d8b46;
  }
  *{box-sizing:border-box;margin:0;padding:0}
  html,body{width:1200px;height:1000px;overflow:hidden}
  body{
    background:linear-gradient(160deg,var(--stage-top),var(--stage-bottom));
    font-family:"Lato",Arial,sans-serif;
    position:relative;
  }
  .card{
    position:absolute;width:760px;height:420px;overflow:hidden;
    background:var(--white);
    box-shadow:0 12px 30px rgba(0,0,0,.45);
  }
  .card-back{left:100px;top:60px}
  .card-front{left:340px;top:520px}
  .card svg.shapes{position:absolute;inset:0}

  /* back side */
  .why-tab{
    position:absolute;left:22px;top:40px;background:var(--white);
    color:var(--navy);font-weight:900;font-size:24px;letter-spacing:1px;
    padding:4px 16px;border-radius:0 8px 8px 0;
  }
  .why-list{position:absolute;left:42px;top:92px;list-style:none;color:var(--white);font-size:15px;line-height:22px}
  .contact{position:absolute;left:60px;top:200px;width:240px;text-align:center;color:var(--white);font-weight:900}
  .contact .lead{font-size:22px;line-height:26px}
  .contact .sub{font-size:17px;line-height:22px}
  .contact .gold{color:var(--gold);font-size:21px;line-height:28px}
  .contact .email{font-size:19px}
  .cards-note{position:absolute;left:70px;bottom:22px;color:var(--white);font-size:12px}
  .cards-note::before{content:"✱ ";font-size:10px}
  .stamp-box{position:absolute;right:60px;top:22px;width:90px;height:92px;border:1.5px solid var(--ink)}
  .address-line{position:absolute;height:1.5px;background:var(--ink)}
  .brand{font-family:"Lato",Arial,sans-serif;font-weight:900;position:absolute;display:flex;align-items:center;gap:8px}
  .brand .mark{width:14px;height:14px}
  .brand-back{right:40px;bottom:40px;color:var(--navy);font-size:30px}
  .brand-back .mark{background:var(--navy)}

  /* front side */
  .brand-front{left:34px;top:28px;color:var(--white);font-size:30px}
  .brand-front .mark{background:var(--white)}
  .headline{position:absolute;left:30px;top:78px;font-family:"Tinos","Times New Roman",serif;font-weight:400;color:var(--white);font-size:26px;line-height:30px}
  .services-title{position:absolute;left:30px;top:176px;color:var(--gold);font-weight:900;font-size:19px;line-height:21px}
  .services{position:absolute;left:34px;top:224px;list-style:none;color:var(--white);font-size:16px;line-height:20px}
  .services li::before{content:"✔";margin-right:8px;font-size:12px}
  .call-label{position:absolute;left:170px;top:336px;color:var(--white);font-weight:900;font-size:20px;line-height:24px}
  .call-phone{position:absolute;left:30px;top:370px;display:flex;align-items:center;gap:10px;color:var(--gold);font-weight:900;font-size:26px;line-height:32px}
</style>
</head>
<body>

<!-- Back: mailing side -->
<section class="card card-back">
  <svg class="shapes" viewBox="0 0 760 420" width="760" height="420">
    <path d="M0 0 H280 Q400 180 370 420 H0 Z" fill="var(--navy)"/>
    <path d="M296 0 Q416 180 386 420" fill="none" stroke="var(--navy)" stroke-width="3"/>
    <g stroke="var(--white)" stroke-width="4">
      <circle cx="316" cy="63" r="52" fill="#a9865e" role="img" aria-label="Photo of a wooden deck under construction"/>
      <circle cx="362" cy="195" r="52" fill="#c39a6c" role="img" aria-label="Photo of house framing with a worker on a ladder"/>
      <circle cx="376" cy="326" r="52" fill="#7a4a26" role="img" aria-label="Photo of a wooden front entry door"/>
    </g>
  </svg>
  <div class="why-tab">WHY US?</div>
  <ul class="why-list">
    <li>Handyman Services</li>
    <li>Fully Insured and Licensed</li>
    <li>High Quality Products</li>
    <li>Free Estimate</li>
  </ul>
  <div class="contact">
    <p class="lead">Free Estimate</p>
    <p class="sub">Call us</p>
    <p class="gold">(617)442-9073</p>
    <p class="sub">or Mail us</p>
    <p class="gold email">morvinkt@mailbrook.net</p>
  </div>
  <p class="cards-note">We Accept all Major Credit Cards</p>
  <div class="stamp-box"></div>
  <div class="address-line" style="left:480px;top:140px;width:180px"></div>
  <div class="address-line" style="left:500px;top:172px;width:180px"></div>
  <div class="address-line" style="left:520px;top:204px;width:180px"></div>
  <div class="address-line" style="left:540px;top:236px;width:180px"></div>
  <div class="brand brand-back"><span class="mark"></span>RWT</div>
</section>

<!-- Front: services side -->
<section class="card card-front">
  <svg class="shapes" viewBox="0 0 760 420" width="760" height="420">
    <defs>
      <linearGradient id="deckScene" x1="0" y1="0" x2="0" y2="1">
        <stop offset="0" stop-color="var(--siding)"/>
        <stop offset=".5" stop-color="var(--deck)"/>
        <stop offset="1" stop-color="var(--lawn)"/>
      </linearGradient>
    </defs>
    <rect x="300" y="0" width="460" height="420" fill="url(#deckScene)" role="img" aria-label="Photo of a house with a new wooden deck, stairs, railing and patio furniture"/>
    <path d="M0 0 H340 Q420 210 380 420 H0 Z" fill="var(--navy)"/>
    <g stroke="var(--gold)" stroke-width="4">
      <circle cx="362" cy="72" r="50" fill="#8f8f8f" role="img" aria-label="Photo of a shingle roof"/>
      <circle cx="392" cy="206" r="50" fill="#cbbd94" role="img" aria-label="Photo of a worker installing siding"/>
      <circle cx="392" cy="340" r="50" fill="#b9c4cc" role="img" aria-label="Photo of a worker installing a gutter"/>
    </g>
  </svg>
  <div class="brand brand-front"><span class="mark"></span>RWT</div>
  <h1 class="headline">Your Total<br>Home Improvement<br>is here !</h1>
  <p class="services-title">Services What<br>we do???</p>
  <ul class="services">
    <li>Roofing</li><li>Siding</li><li>Gutter</li><li>Decks</li><li>Additions</li><li>Windows</li><li>Doors</li>
  </ul>
  <p class="call-label">Call us on</p>
  <p class="call-phone">
    <svg width="24" height="24" viewBox="0 0 24 24" aria-hidden="true">
      <circle cx="12" cy="12" r="10.5" fill="none" stroke="var(--white)" stroke-width="1.5"/>
      <path d="M8.5 7 L10 6.6 L11 9 L10 10 Q11 12.5 13.6 13.8 L14.6 12.8 L17 13.8 L16.6 15.4 Q12 16.5 8.4 11.5 Q7.6 9 8.5 7 Z" fill="var(--white)"/>
    </svg>
    617-442-9073
  </p>
</section>

</body>
</html>
```